create clean, simple business card template

using the logo created now we need to create a simple, elegant business card design to suit

Industry/Entity Type

Business

Font styles to use
Other font styles liked:
• segoe ui

Requirements
Must have
• Front:
"Name:"
"Title:"
"Mobile:"
"email:"
and the logo

Back:
Logo
Nice to have
• Text in black but other graphics etc to match colours in logo as provided

```html
<!DOCTYPE html>
<html lang="en">
<head>
<meta charset="utf-8">
<title>Halden Property – Business Cards</title>
<link rel="stylesheet" href="https://fonts.googleapis.com/css2?family=Open+Sans:wght@400;600;700&display=swap">
<style>
  :root {
    --backdrop: #e9e5dc;
    --card-white: #ffffff;
    --kraft: #b8a783;
    --brand-tan: #9c8a64;
    --ink: #111111;
    --ink-soft: #444444;
    --rule: #555555;
  }
  * { box-sizing: border-box; margin: 0; padding: 0; }
  html, body { width: 1200px; height: 1000px; overflow: hidden; }
  body {
    background: var(--backdrop);
    font-family: "Open Sans", "Segoe UI", sans-serif;
    position: relative;
  }
  .card {
    position: absolute;
    width: 640px;
    height: 366px;
    background: var(--kraft);
    padding: 10px;
    box-shadow: 0 6px 18px rgba(0,0,0,0.18);
  }
  .card--front { left: 90px; top: 110px; }
  .card--back  { left: 470px; top: 520px; display: flex; flex-direction: column; gap: 14px; }

  .panel { background: var(--card-white); }
  .card--front .panel { height: 100%; display: flex; align-items: center; justify-content: center; }

  .wordmark { display: flex; align-items: center; gap: 14px; }
  .wordmark__dot {
    width: 30px; height: 30px; border-radius: 50%;
    background: var(--brand-tan);
  }
  .wordmark__name {
    font-weight: 600;
    font-size: 40px;
    color: var(--brand-tan);
    letter-spacing: 1px;
  }

  .panel--brand { height: 140px; display: flex; align-items: center; justify-content: center; }
  .panel--brand .wordmark__name { font-size: 36px; }
  .panel--details {
    flex: 1;
    display: flex;
    align-items: flex-end;
    justify-content: space-between;
    padding: 0 28px 28px 34px;
    position: relative;
  }
  .person__name { font-weight: 700; font-size: 30px; color: var(--ink); line-height: 1.1; }
  .person__title { font-size: 17px; color: var(--ink-soft); margin-top: 2px; }
  .divider {
    position: absolute; left: 268px; bottom: 34px;
    width: 1px; height: 70px; background: var(--rule);
  }
  .contact { list-style: none; text-align: right; font-size: 17px; color: var(--ink); line-height: 1.55; }
  .contact li { display: flex; align-items: center; justify-content: flex-end; gap: 8px; }
  .contact svg { width: 18px; height: 18px; fill: var(--brand-tan); }
</style>
</head>
<body>
  <section class="card card--front" aria-label="Business card front">
    <div class="panel">
      <div class="wordmark">
        <span class="wordmark__dot"></span>
        <span class="wordmark__name">Halden Property</span>
      </div>
    </div>
  </section>

  <section class="card card--back" aria-label="Business card back">
    <div class="panel panel--brand">
      <div class="wordmark">
        <span class="wordmark__dot"></span>
        <span class="wordmark__name">Halden Property</span>
      </div>
    </div>
    <div class="panel panel--details">
      <div class="person">
        <p class="person__name">Mark Ellery</p>
        <p class="person__title">Property Manager</p>
      </div>
      <span class="divider"></span>
      <ul class="contact">
        <li>+ 000 - 4821 - 9036 :
          <svg viewBox="0 0 24 24" aria-hidden="true"><path d="M6.6 10.8a15.1 15.1 0 0 0 6.6 6.6l2.2-2.2c.3-.3.7-.4 1-.2 1.1.4 2.3.6 3.6.6.6 0 1 .4 1 1V20c0 .6-.4 1-1 1A17 17 0 0 1 3 4c0-.6.4-1 1-1h3.5c.6 0 1 .4 1 1 0 1.3.2 2.5.6 3.6.1.3 0 .7-.2 1z"/></svg>
        </li>
        <li>markellery@haldenproperty.com :
          <svg viewBox="0 0 24 24" aria-hidden="true"><path d="M2 5h20v14H2z M3.5 6.5 12 13l8.5-6.5" fill="var(--brand-tan)" stroke="#fff" stroke-width="1.2"/></svg>
        </li>
      </ul>
    </div>
  </section>
</body>
</html>
```